Brent Halvorsen Professional Coaching

I would like a website with a mountain theme geared towards professional executives reaching higher peaks and goals. This is a 3 page website with brand essence information on the opening page, the coaching process on a second page and "about me" and lead capture form on a third page

Target Market(s)

C-Level audience, involved in tech, government, manufacturing, and transportation type of corporations

Coding

Number of Pages Required

3 page

Font styles to use
Sans Serif

Colors
a7a7a7
1b1b1b
e8e8e8
3176b5
abd036
0355a3

Requirements
Must have
• Looking for a user friendly site that I can manage/update going forward. Must have:
• 1. "Is coaching right for you?" - page 1
• 2. "Our Process" page 2 - I will describe how we approach coaching
• 3. "Contact us" page 3 where I can capture contact information from potential clients
• 4. Clean and professional with more modern font
• 5. Links to personal social media sites
• 6. Ability to upload/download .pdf documents as resources
• 7. Ability to add on new pages in the future (such as a blog page)
Nice to have
• I want a place to store articles I write or use.
• LinkedIn or Twitter Feed
Should not have
• Not fluffy or too 'zen' like personal life coaches tend to present.

```html
<!DOCTYPE html>
<html lang="en">
<head>
<meta charset="utf-8">
<title>Brent Halvorsen Professional Coaching</title>
<link href="https://fonts.googleapis.com/css2?family=Poppins:wght@600;700;800&family=PT+Sans:wght@400;700&display=swap" rel="stylesheet">
<style>
:root{
  --ink:#1b1b1b;
  --grey:#a7a7a7;
  --light:#e8e8e8;
  --page:#f3f1f8;
  --blue:#3176b5;
  --navy:#0355a3;
  --deep:#1d3f73;
  --white:#ffffff;
}
*{margin:0;padding:0;box-sizing:border-box}
html,body{width:1200px;height:3879px;overflow:hidden}
body{background:var(--page);font-family:"PT Sans",Arial,sans-serif;color:var(--ink);position:relative}
.abs{position:absolute}
.heading{font-family:"Poppins",Arial,sans-serif;font-weight:700;text-transform:uppercase;color:var(--ink)}
.btn{position:absolute;background:var(--navy);color:var(--white);font-family:"Poppins",Arial,sans-serif;font-weight:600;text-transform:uppercase;display:flex;align-items:center;justify-content:center;letter-spacing:.5px}

/* Hero */
.hero{top:0;left:0;width:1200px;height:698px;background:linear-gradient(180deg,#eef0f8 0%,#c9d6ea 22%,#7d9cc9 45%,#3b66a8 68%,#1d3b6e 88%,#172d52 100%)}
.brand{top:28px;left:38px;font-family:"Poppins",Arial,sans-serif;font-weight:700;font-size:24px;color:var(--ink)}
.nav{top:28px;right:34px;display:flex;gap:30px;font-family:"Poppins",Arial,sans-serif;font-weight:600;font-size:14px;text-transform:uppercase}
.hero-title{top:205px;left:0;width:1200px;text-align:center;font-size:56px;line-height:62px;font-weight:800}
.dots{top:642px;left:554px;display:flex;gap:12px}
.dots span{width:9px;height:9px;border-radius:50%;background:var(--white)}
.dots span.off{background:transparent;border:1.5px solid var(--white)}

/* Services */
.section-title{left:0;width:1200px;text-align:center;font-size:34px}
.rule{left:585px;width:30px;height:3px;background:var(--grey)}
.service{top:866px;width:300px;text-align:center}
.service .ring{width:130px;height:130px;border:2px solid var(--blue);border-radius:50%;margin:0 auto;display:flex;align-items:center;justify-content:center}
.service h3{font-family:"Poppins",Arial,sans-serif;font-weight:700;font-size:18px;margin-top:42px}
.service p{font-size:14px;line-height:17px;color:#333;margin:22px auto 0;width:250px}
.service .btn{position:relative;width:96px;height:26px;font-size:11px;margin:28px auto 0}
.snow-band{top:1241px;left:0;width:1200px;height:260px;background:linear-gradient(180deg,#f3f1f8 0%,#c7d3e6 30%,#8ea6c8 50%,#dfe5ef 75%,#ffffff 100%)}

/* Welcome */
.welcome-bg{top:1500px;left:0;width:1200px;height:520px}
.portrait{top:1538px;left:0;width:517px;height:390px;background:radial-gradient(ellipse at 60% 45%,#8aa06a 0%,#4f7a3c 45%,#2d4a2a 80%);border-radius:0 180px 40px 0}
.welcome-tag{top:1550px;left:574px;width:190px;height:32px;background:var(--blue);color:var(--white);font-family:"Poppins",Arial,sans-serif;font-weight:700;font-size:19px;display:flex;align-items:center;justify-content:center;text-transform:uppercase}
.welcome-name{top:1592px;left:585px;font-family:"Poppins",Arial,sans-serif;font-weight:800;font-size:50px;color:#8795ab;text-transform:uppercase;letter-spacing:1px}
.welcome-copy{top:1676px;left:590px;width:475px;font-size:15.5px;line-height:20.5px;color:#333}
.welcome .btn{top:1846px;left:590px;width:116px;height:32px;font-size:13px}

/* Change */
.change-title{top:2046px;font-size:32px}
.benefit{top:2190px;text-align:center;font-family:"Poppins",Arial,sans-serif;font-weight:600;font-size:14px;line-height:17px;color:#333}
.benefit svg{display:block;margin:0 auto 14px}
.divider{top:2185px;width:1px;height:137px;background:#cfcfd8}

/* CTA */
.cta{top:2418px;left:0;width:1200px;height:530px;background:linear-gradient(180deg,#f3f1f8 0%,#b47b55 8%,#6b3b26 25%,#3a231c 45%,#1f1a1c 70%,#141215 100%)}
.cta h2{top:2632px;left:0;width:1200px;text-align:center;font-family:"Poppins",Arial,sans-serif;font-weight:700;font-size:28px;color:var(--white)}
.cta p{top:2694px;left:0;width:1200px;text-align:center;font-size:18px;line-height:23px;color:var(--white)}
.cta .btn{top:2786px;left:496px;width:210px;height:42px;font-size:14px}

/* Contact */
.contact-title{top:2998px;left:238px;font-size:34px}
.field{background:var(--white);border:1px solid #c9c9cf;font-size:11px;color:#555;text-transform:uppercase;padding:12px 14px;font-family:"PT Sans",Arial,sans-serif}
.submit{top:3336px;left:817px;width:145px;height:46px;font-size:20px;font-weight:700}

/* Footer */
.footer{top:3440px;left:0;width:1200px;height:439px;background:linear-gradient(180deg,#f3f1f8 0%,#b9dcee 10%,#6fb3d9 35%,#2f82bd 60%,#155b96 85%,#0e3f73 100%)}
.footer-name{top:3596px;left:0;width:1200px;text-align:center;font-family:"Poppins",Arial,sans-serif;font-weight:700;font-size:34px;color:var(--white)}
.footer-nav{top:3680px;left:0;width:1200px;display:flex;justify-content:center;gap:14px;font-family:"Poppins",Arial,sans-serif;font-weight:600;font-size:12px;color:var(--white);text-transform:uppercase}
.follow{top:3732px;left:500px;display:flex;align-items:center;gap:12px;color:var(--white);font-family:"Poppins",Arial,sans-serif;font-weight:600;font-size:12px;text-transform:uppercase}
.follow span.social{width:26px;height:26px;border-radius:50%;background:var(--navy);display:block}
.copyright{top:3802px;left:0;width:1200px;text-align:center;font-size:12px;color:var(--light)}
</style>
</head>
<body>

<header>
  <div class="abs hero" role="img" aria-label="Photo of a hiker standing on a rock summit facing snowy mountain peaks"></div>
  <div class="abs brand">BRENT HALVORSEN</div>
  <nav class="abs nav"><span>Home</span><span>About Me</span><span>Coaching Process</span></nav>
  <h1 class="abs heading hero-title">Professional<br>Coaching</h1>
  <div class="abs dots"><span></span><span></span><span class="off"></span><span></span><span></span></div>
</header>

<section class="services">
  <h2 class="abs heading section-title" style="top:746px">Services</h2>
  <div class="abs rule" style="top:805px"></div>

  <div class="abs service" style="left:120px">
    <div class="ring"><svg width="58" height="50" viewBox="0 0 58 50" fill="none" stroke="#3176b5" stroke-width="3"><rect x="3" y="12" width="52" height="35" rx="5"/><path d="M20 12V6a3 3 0 0 1 3-3h12a3 3 0 0 1 3 3v6M3 26h52"/></svg></div>
    <h3>Executive Coaching</h3>
    <p>Sed ut perspiciatis unde omnis iste natus error sit voluptatem accusa ntium doloremque lauda ntium, totam rem aperiam eaque ipsa quae.</p>
    <div class="btn">Read More</div>
  </div>

  <div class="abs service" style="left:449px">
    <div class="ring"><svg width="70" height="62" viewBox="0 0 70 62" fill="none" stroke="#3176b5" stroke-width="2.5"><circle cx="35" cy="9" r="6"/><path d="M27 26a8 8 0 0 1 16 0M35 26v8M12 34h46M12 34v6M35 34v6M58 34v6"/><circle cx="12" cy="45" r="4.5"/><circle cx="35" cy="45" r="4.5"/><circle cx="58" cy="45" r="4.5"/><path d="M5 60a7 7 0 0 1 14 0M28 60a7 7 0 0 1 14 0M51 60a7 7 0 0 1 14 0"/></svg></div>
    <h3>Leadership Development</h3>
    <p>Sed ut perspiciatis unde omnis iste natus error sit voluptatem accusa ntium doloremque lauda ntium, totam rem aperiam eaque ipsa quae.</p>
    <div class="btn">Read More</div>
  </div>

  <div class="abs service" style="left:780px">
    <div class="ring"><svg width="66" height="62" viewBox="0 0 66 62" fill="none" stroke="#3176b5" stroke-width="2.5"><rect x="6" y="4" width="54" height="34"/><path d="M3 4h60M14 30l10-10 8 6 14-14 8 6M33 38v8M20 60l8-14M46 60l-8-14"/></svg></div>
    <h3>Workshops &amp; Facilitation</h3>
    <p>Sed ut perspiciatis unde omnis iste natus error sit voluptatem accusa ntium doloremque lauda ntium, totam rem aperiam eaque ipsa quae.</p>
    <div class="btn">Read More</div>
  </div>

  <div class="abs snow-band" role="img" aria-label="Photo of snowy mountain ridge above clouds"></div>
</section>

<section class="welcome">
  <svg class="abs welcome-bg" width="1200" height="520" viewBox="0 0 1200 520"><polygon points="0,0 1200,0 1200,580 0,430" fill="#ffffff"/></svg>
  <div class="abs portrait" role="img" aria-label="Portrait photo of the coach in a navy blazer against green foliage"></div>
  <div class="welcome-tag abs">Welcome To</div>
  <div class="abs welcome-name">Brent Halvorsen</div>
  <p class="abs welcome-copy">At vero eos et accusamus et iusto odio dignissimos ducimus qui blanditiis praesentium voluptatum deleniti atque corrupti quos dolores et quas molestias excepturi sint occaecati cupiditate non provident, similique sunt in culpa qui officia deserunt mollitia animi, id est laborum et dolorum fuga. Et harum quidem rerum facilis est et expedita distinctio. Nam libero tempore, cum soluta nobis est eligendi optio cumque nihil impedit.</p>
  <div class="btn">Read More</div>
</section>

<section class="change">
  <h2 class="abs heading section-title change-title">Powerful Positive Change</h2>

  <div class="abs benefit" style="left:170px;width:180px">
    <svg width="54" height="50" viewBox="0 0 54 50" fill="none" stroke="#3176b5" stroke-width="2.5"><circle cx="27" cy="12" r="9"/><circle cx="11" cy="18" r="6"/><circle cx="43" cy="18" r="6"/><path d="M13 48V38a14 14 0 0 1 28 0v10z"/><path d="M3 44v-6a8 8 0 0 1 9-8M51 44v-6a8 8 0 0 0-9-8"/></svg>
    Improved<br>Leadership Capacity
  </div>
  <div class="abs divider" style="left:388px"></div>

  <div class="abs benefit" style="left:410px;width:170px">
    <svg width="54" height="50" viewBox="0 0 54 50" fill="none" stroke="#3176b5" stroke-width="2.5"><circle cx="27" cy="20" r="7"/><path d="M15 44a12 12 0 0 1 24 0M27 2v5M12 8l3 4M42 8l-3 4M5 20h5M44 20h5"/></svg>
    Increase<br>Self Esteem
  </div>
  <div class="abs divider" style="left:595px"></div>

  <div class="abs benefit" style="left:620px;width:180px">
    <svg width="54" height="50" viewBox="0 0 54 50" fill="none" stroke="#3176b5" stroke-width="2.5"><path d="M4 48h46M8 48V36h7v12M21 48V28h7v12 8M34 48V20h7v28M6 26l14-10 10 6 16-16M38 6h8v8"/></svg>
    Growth<br>Performance
  </div>
  <div class="abs divider" style="left:822px"></div>

  <div class="abs benefit" style="left:850px;width:190px">
    <svg width="54" height="50" viewBox="0 0 54 50" fill="none" stroke="#3176b5" stroke-width="2.5"><path d="M27 6a13 13 0 0 0-8 23c2 2 3 4 3 7h10c0-3 1-5 3-7a13 13 0 0 0-8-23zM22 40h10M23 45h8"/></svg>
    Creating a Culture<br>of Inspiration &amp; Re<br>Imagination
  </div>
</section>

<section>
  <div class="abs cta" role="img" aria-label="Photo of layered dark mountain ridges at sunset"></div>
  <div class="cta">
    <h2 class="abs" style="top:2632px">Ready To Take It To The Next Level?</h2>
    <p class="abs">At vero eos et accusamus et iusto odio dignissimos ducimus<br>blanditiis praesentium voluptatum deleniti atque</p>
    <div class="btn">Contact Us Today</div>
  </div>
</section>

<section class="contact">
  <h2 class="abs heading contact-title">Contact Me</h2>
  <div class="abs field" style="top:3077px;left:238px;width:236px;height:44px">Name</div>
  <div class="abs field" style="top:3077px;left:483px;width:235px;height:44px">E-mail</div>
  <div class="abs field" style="top:3077px;left:727px;width:235px;height:44px">Phone</div>
  <div class="abs field" style="top:3137px;left:238px;width:724px;height:168px">Message</div>
  <div class="btn submit">Submit</div>
</section>

<footer>
  <div class="abs footer" role="img" aria-label="Photo of misty blue mountain ranges"></div>
  <div class="abs footer-name">BRENT HALVORSEN</div>
  <nav class="abs footer-nav"><span>Home</span><span>\</span><span>About Me</span><span>\</span><span>Coaching Process</span><span>\</span><span>Contact</span></nav>
  <div class="abs follow">Follow <span class="social" aria-label="Social profile"></span><span class="social" aria-label="Social profile"></span><span class="social" aria-label="Social profile"></span></div>
  <div class="abs copyright">Copyrights @ 2019 All Rights Reserved</div>
</footer>

</body>
</html>
```